Company Profile
Korvane Cargo Sdn Bhd is a well-established and experienced freight forwarder in Kuala Lumpur, Malaysia. We specialize in air and sea forwarding, Custom Brokerage and regulatory compliance services, inland transportation, overseas freighting and warehousing and distribution management. With our dedicated qualified and experienced professionals, we are fully committed to serving our clients.

Our Mission
Based on the motto “Quick, Reliable and Polite”, Korvane Cargo is dedicated to upholding the following three points corporate philosophy:1. Adhering to the principle that “the customer always comes first”.2. Contributing to the development of the local community.3. Making it our duty to be responsible and sincere.

Our Edge
• One-Stop Logistics Solutions
• Extensive Network Throughout Malaysia
• Highly Qualified and Experienced Pool of Professionals
• Comprehensive IT Solutions
• Innovative and Customer-focused Solutions
• Flexible and Consistent in Managing Exceptions
• Total Supply Chain Visibility

Target Market : We sell the logistics services to all the industry in Malaysia. (One Stop Logistics Solutions)

Business Card Detail : I would like to see the logo on the front with the general info.

Must Haves :
1) Name, Title, Office, Cell, Fax, Email, Address, Website
2) Must have complete company name show as : Korvane Cargo Sdn Bhd
3) Must have company registration no, show as : 8571620-W

Nice to Haves : Modern Design Business Card

Target Market(s)

We sell the logistics services to all the industry in Malaysia. (One Stop Logistics Solutions)

Contact Information for Business Card

I would like to see the logo on the front with the general info.

Colors

Designer to choose colors to be used in the design.

Requirements
Must have
• 1) Name, Title, Office, Cell, Fax, Email, Address, Website
• 2) Must have complete company name show as : Korvane Cargo Sdn Bhd
• 3) Must have company registration no, show as : 8571620-W
Nice to have
• Modern Design Business Card
Should not have
• Nil

```html
<!DOCTYPE html>
<html lang="en">
<head>
<meta charset="utf-8">
<title>Korvane Cargo – Business Card</title>
<link rel="stylesheet" href="https://fonts.googleapis.com/css2?family=Roboto:wght@400;500;700&display=swap">
<style>
  :root {
    --page: #e6e6e6;
    --navy: #0d4f8f;
    --navy-deep: #0b4a8a;
    --navy-bright: #0f67b5;
    --sky: #2aa4e0;
    --white: #ffffff;
    --ink-grey: #4a4a4a;
  }
  * { margin: 0; padding: 0; box-sizing: border-box; }
  html, body {
    width: 1125px; height: 1200px; overflow: hidden;
    background: var(--page);
    font-family: "Roboto", Arial, sans-serif;
  }
  .card {
    position: absolute; left: 172px; width: 826px; height: 472px;
    border-radius: 24px; overflow: hidden;
    box-shadow: 0 3px 6px rgba(0,0,0,0.25);
  }
  .card--front { top: 106px; background: var(--navy); }
  .card--back {
    top: 638px;
    background: linear-gradient(120deg, var(--navy-deep) 0%, var(--navy-deep) 45%, var(--navy-bright) 100%);
  }
  .front-waves { position: absolute; inset: 0; }
  .reg-no {
    position: absolute; left: 575px; top: 34px;
    font-size: 17px; color: var(--ink-grey);
  }
  .brand {
    position: absolute; left: 62px; top: 88px;
    display: flex; align-items: center; gap: 16px;
  }
  .brand-circle {
    width: 66px; height: 66px; border-radius: 50%;
    border: 4px solid var(--navy);
  }
  .brand-name {
    font-size: 36px; font-weight: 700; color: var(--navy); letter-spacing: 1px;
  }
  .person { position: absolute; left: 63px; top: 190px; }
  .person-name { font-size: 28px; font-weight: 700; color: var(--navy); line-height: 32px; }
  .person-title { font-size: 20px; color: var(--sky); line-height: 26px; }
  .contact {
    position: absolute; right: 31px; top: 238px;
    text-align: right; color: var(--white); font-size: 19px; line-height: 26px;
  }
  .contact-company { font-weight: 500; margin-top: 5px; }
  .back-brand {
    position: absolute; left: 0; right: 0; top: 186px;
    display: flex; justify-content: center; align-items: center; gap: 22px;
  }
  .back-circle {
    width: 84px; height: 84px; border-radius: 50%;
    border: 5px solid var(--white);
  }
  .back-name { font-size: 44px; font-weight: 700; color: var(--white); letter-spacing: 1px; }
  .tagline {
    position: absolute; left: 0; right: 0; top: 396px;
    text-align: center; color: var(--white); font-size: 20px;
  }
</style>
</head>
<body>
  <section class="card card--front">
    <svg class="front-waves" viewBox="0 0 826 472" width="826" height="472" aria-hidden="true">
      <path d="M0,0 H826 V40 C600,205 360,412 170,412 C90,412 25,385 0,345 Z" fill="var(--white)"/>
      <path d="M0,0 H826 V40 C600,202 360,406 170,406 C90,406 25,380 0,340 Z" fill="var(--sky)"/>
      <path d="M0,0 H826 V40 C600,198 360,394 165,394 C85,394 22,368 0,330 Z" fill="var(--white)"/>
    </svg>
    <p class="reg-no">Reg No: 8571620-W</p>
    <div class="brand">
      <span class="brand-circle"></span>
      <span class="brand-name">KORVANE CARGO</span>
    </div>
    <div class="person">
      <p class="person-name">DANIEL TAN</p>
      <p class="person-title">Managing Director</p>
    </div>
    <div class="contact">
      <p>(+603) 5521 7380 / 7381</p>
      <p>(+6012) 468 2095</p>
      <p>(+603) 5521 7382</p>
      <p>daniel.tan@korvanecargo.com.my</p>
      <p>www.korvanecargo.com.my</p>
      <p class="contact-company">Korvane Cargo Sdn Bhd</p>
      <p>No.22B, 2nd Floor, Jalan Seri Mutiara 3/KS2</p>
      <p>Taman Seri Mutiara, 41050 Klang, Selangor Darul Ehsan, Malaysia</p>
    </div>
  </section>

  <section class="card card--back">
    <div class="back-brand">
      <span class="back-circle"></span>
      <span class="back-name">KORVANE CARGO</span>
    </div>
    <p class="tagline">One Stop Logistics Specialist</p>
  </section>
</body>
</html>
```